Business Card Revision

Need to redesign my business cards for a new professional look. We are a courier company. You can go to www.qvrunners.com to see what we do. The trucks have an old company name (Sprout) on them but that is the company we are just now
changing the name.

Target Market(s)

Potential clients. We service the automotive, plumbing, printing, air freight industries as well as many others.

Industry/Entity Type

Business

Contact Information for Business Card

QVmotion
20864 Lark Fenmore Parkway
Cincinnati, Oh 45873

Thomas R. Wendall
President

tom@qvrunners.com

Main: (513) 555-0147

```html
<!DOCTYPE html>
<html lang="en">
<head>
<meta charset="utf-8">
<title>QV Runners Business Card</title>
<link rel="stylesheet" href="https://fonts.googleapis.com/css2?family=Roboto:wght@400;700;900&display=swap">
<style>
  :root {
    --bg: #e9e6e1;
    --green: #3cb54a;
    --green-dark: #2fa43f;
    --blue: #1a7fc6;
    --blue-dark: #1470b3;
    --white: #ffffff;
    --shadow: rgba(0, 0, 0, 0.22);
  }
  * { margin: 0; padding: 0; box-sizing: border-box; }
  html, body {
    width: 1200px;
    height: 950px;
    overflow: hidden;
    background: var(--bg);
    font-family: "Roboto", Arial, sans-serif;
  }
  .canvas {
    position: relative;
    width: 1200px;
    height: 950px;
  }
  .card {
    position: absolute;
    left: 250px;
    width: 700px;
    height: 400px;
    overflow: hidden;
    box-shadow: 0 10px 28px var(--shadow);
  }
  .card-front {
    top: 45px;
    background: var(--green);
  }
  .card-back {
    top: 505px;
    background: var(--white);
  }
  .brand-name {
    position: absolute;
    font-weight: 900;
    font-size: 58px;
    letter-spacing: 2px;
    text-transform: uppercase;
    white-space: nowrap;
  }
  .card-front .brand-name {
    left: 0;
    right: 0;
    top: 140px;
    text-align: center;
    color: var(--white);
  }
  .website {
    position: absolute;
    right: 60px;
    top: 290px;
    color: var(--white);
    font-size: 17px;
    letter-spacing: 7px;
  }
  .card-back .brand-name {
    left: 70px;
    top: 70px;
    color: var(--blue);
  }
  .back-band {
    position: absolute;
    left: 0;
    top: 0;
    width: 700px;
    height: 400px;
  }
  .holder {
    position: absolute;
    right: 40px;
    top: 232px;
    text-align: right;
    color: var(--white);
  }
  .holder-name {
    font-weight: 700;
    font-size: 24px;
  }
  .holder-title {
    font-size: 17px;
    margin-top: 3px;
  }
  .contact {
    position: absolute;
    left: 40px;
    top: 248px;
    color: var(--white);
    font-size: 17px;
    line-height: 26px;
    list-style: none;
  }
  .contact li {
    display: flex;
    align-items: center;
    gap: 8px;
  }
  .contact svg {
    width: 16px;
    height: 16px;
    flex: none;
  }
</style>
</head>
<body>
<main class="canvas">

  <section class="card card-front" aria-label="Business card front">
    <div class="brand-name">QV Runners</div>
    <div class="website">www.qvrunners.com</div>
  </section>

  <section class="card card-back" aria-label="Business card back">
    <svg class="back-band" viewBox="0 0 700 400" aria-hidden="true">
      <path d="M0 196 H528 L542 182 L556 196 H700 V400 H0 Z" fill="var(--green)"/>
      <path d="M0 201 H530 L542 189 L554 201 H700 V400 H0 Z" fill="var(--blue)"/>
    </svg>

    <div class="brand-name">QV Runners</div>

    <div class="holder">
      <div class="holder-name">Thomas R. Wendall</div>
      <div class="holder-title">President</div>
    </div>

    <ul class="contact">
      <li>QVmotion</li>
      <li>20864 Lark Fenmore Parkway</li>
      <li>Cincinnati, Oh 45873</li>
      <li>
        <svg viewBox="0 0 16 16" aria-hidden="true">
          <path d="M2 5 Q8 1 14 5 L12 7 L10 5.5 H6 L4 7 Z" fill="var(--white)"/>
          <rect x="3" y="8" width="10" height="6" rx="1" fill="var(--white)"/>
          <circle cx="8" cy="11" r="1.6" fill="var(--blue)"/>
        </svg>
        (513) 555-0147
      </li>
      <li>
        <svg viewBox="0 0 16 16" aria-hidden="true">
          <rect x="1" y="3" width="14" height="10" rx="1" fill="var(--white)"/>
          <path d="M1.5 3.5 L8 9 L14.5 3.5" fill="none" stroke="var(--blue)" stroke-width="1.3"/>
        </svg>
        tom@qvrunners.com
      </li>
    </ul>
  </section>

</main>
</body>
</html>
```